Website Design for a chemical distribution company

Designer must provide full implementation/coding depending on the platform chosen by the client we'd prefer wordpress type CMS system.

We need a modern and bold website setup for our chemical distribution company. It will need to be like a web store however, no purchases take place on the website only inquiries. So for example the customer can go to a product and click on a button that brings up an inquiry window, they populate that with their information and it sends me an email with the inquiry.

We need it done 3 times pretty much the same but maybe a different colour scheme for each industry. for example on the welcome screen we want 3 icons /pictures ie: plastic, resin, industrial. When the customer clicks on the industry they need it directs them to the specific area that is perhaps on a subdomain or somewhere on the main domain but with no relation to the other industries I hope this makes sense. The layout would be the same but their should be some difference such as colours etc.

The site needs to have a powerful search engine that is very accurate.

It will have about 40,000 products and needs to be able to upload our products via an excel spreed sheet.

We need it to look graphically amazing and very easy to use for the customer.

It will also need to have a blog section that we can upload blogs to daily with different sub categories for things such as experiments, news etc.

The front page needs to be have a banner/advertisement window that is easy for us to change with new specials/deals that we bring out.

Basically the site needs to be easy to navigate, easy to get to products and inquire and needs to have a wow factor.

We also need a special requess page that gives the customers the facility to request a product that they can't find on our website.

I need to stress the importance of a search engine on the site that can handle searching through all the products.

We will also give you the words and you will need to put those on to the pages.

You will also be required to upload our catalogue via CSV or Excel to the site on final completion.

Please find similar websites below for companies that similar to us:

www.tarvelo.com
www.brenti-koval.com
http://www.northumlab.com.au

Just to clarify only one of the websites will have 40-50k products the other 2 industries will only have about 200-500 products each. Added Sunday, February 14, 2016

Reason: Finalising designs and need more time.

Target Market(s)

Chemicals, Food, Pharmaceuticals, Business to Business

Industry/Entity Type

It Company

Coding

Coded - Design and coding required

Number of Pages Required

5+ page

Font styles to use
Sans Serif

Requirements
Must have
• Powerful search engine
• Great design
• Easy to use CMS
• SEO
• Mobile Device Compatible

```html
<!DOCTYPE html>
<html lang="en">
<head>
<meta charset="utf-8">
<title>Chemora – A Chemical Distribution Company</title>
<link href="https://fonts.googleapis.com/css2?family=Source+Sans+3:wght@300;400;600&display=swap" rel="stylesheet">
<style>
:root{
  --blue:#0a6fc2;
  --blue-dark:#075a9f;
  --ink:#222;
  --muted:#666;
  --light:#f7f7f7;
  --footer:#f2f2f2;
  --line:#e4e4e4;
  --white:#fff;
}
*{box-sizing:border-box;margin:0;padding:0}
html,body{width:808px;height:1200px;overflow:hidden;background:var(--white)}
body{font-family:"Source Sans 3",Arial,sans-serif;color:var(--ink);position:relative}
.abs{position:absolute}

/* header */
.site-header{position:absolute;left:0;top:0;width:808px;height:65px;background:var(--white)}
.brand{left:98px;top:16px;display:flex;align-items:center;gap:6px;font-size:24px;font-weight:600;color:var(--blue)}
.brand-dot{width:12px;height:12px;border-radius:50%;background:var(--blue)}
.main-nav{left:272px;top:26px;display:flex;gap:0;font-size:9.5px}
.main-nav a{color:var(--ink);text-decoration:none;margin-right:29px}
.main-nav a.active{color:var(--blue)}
.search-toggle{left:678px;top:17px;width:30px;height:30px;border-radius:50%;background:#3c93d6;display:flex;align-items:center;justify-content:center}

/* hero */
.hero{left:0;top:65px;width:808px;height:367px;background:linear-gradient(90deg,#2d6f9c 0%,#8fb7d3 35%,#cfe0ec 60%,#9fc0d8 100%)}
.hero-title{left:96px;top:160px;width:240px;text-align:center;color:var(--white);font-weight:300;font-size:31px;line-height:29px;letter-spacing:.5px}
.hero-arrow{top:182px}

/* search bar */
.search-bar{left:0;top:432px;width:808px;height:67px;background:linear-gradient(#fbfbfb,#eeeeee);border-bottom:1px solid var(--line)}
.search-label{left:98px;top:459px;font-size:12.5px;font-weight:600}
.field{top:452px;height:33px;background:var(--white);border:1px solid #e2e2e2;border-radius:3px;font-size:9px;color:var(--muted);padding:11px 0 0 24px}
.search-btn{left:623px;top:452px;width:87px;height:33px;background:var(--blue);color:var(--white);border-radius:3px;font-size:9px;font-weight:600;text-align:center;line-height:33px}

/* industries */
.industries{left:0;top:499px;width:808px;height:145px;background:var(--light)}
.industry-icon{top:532px;width:74px;height:74px;border-radius:50%;background:var(--blue);display:flex;align-items:center;justify-content:center}
.industry-shadow{top:606px;width:60px;height:8px;border-radius:50%;background:radial-gradient(rgba(0,0,0,.35),transparent 70%)}
.industry-title{top:549px;font-size:12.5px;font-weight:400}
.industry-text{top:568px;width:112px;font-size:6.5px;line-height:9.6px;color:#888}

/* sections */
.section-title{font-size:12px;top:676px}
.welcome-photo{left:98px;top:710px;width:403px;height:148px;border:2px solid #e0e0e0;background:linear-gradient(90deg,#c9d7e3,#eef3f7 50%,#7fb0d9 70%,#e6edf3)}
.body-copy{font-size:6.4px;line-height:12.8px;color:#333}
.btn{height:21px;background:var(--blue);color:var(--white);border-radius:3px;font-size:8.5px;line-height:21px;text-align:center}
.blog-photo{left:517px;top:710px;width:194px;height:128px;background:linear-gradient(135deg,#0d3c6e,#2f78b3 50%,#a9cbe6)}
.date-badge{left:526px;top:710px;width:39px;height:40px;background:var(--blue);color:var(--white);font-size:7.5px;line-height:9.5px;text-align:center;padding-top:4px}
.blog-heading{left:517px;top:850px;width:200px;font-size:9.5px;line-height:14.5px;color:var(--blue)}
.pager{left:694px;top:676px;font-size:11px;letter-spacing:6px}

/* ad banner */
.ad-banner{left:98px;top:987px;width:613px;height:79px;background:linear-gradient(90deg,#e7eff6,#c7dceb 50%,#dde8f1)}
.ad-brand{left:110px;top:1012px;display:flex;align-items:center;gap:5px;font-size:22px;font-weight:600;color:var(--blue)}
.ad-title{left:460px;top:1008px;font-size:17px;color:var(--blue)}
.ad-sub{left:460px;top:1028px;font-size:12px;font-weight:300;color:#557}
.ad-tag{left:678px;top:987px;width:33px;height:27px;background:var(--blue);color:var(--white);font-size:8.5px;text-align:center;line-height:27px}

/* footer */
.site-footer{left:0;top:1096px;width:808px;height:104px;background:var(--footer)}
.social{left:336px;top:1119px;display:flex;gap:13px}
.social span{width:12px;height:12px;border-radius:50%;background:var(--blue)}
.footer-nav{left:0;top:1150px;width:808px;text-align:center;font-size:8px;color:#333}
.footer-nav i{font-style:normal;margin:0 12px}
.copyright{left:0;top:1173px;width:808px;text-align:center;font-size:7.5px;color:#333}
</style>
</head>
<body>

<header class="site-header">
  <div class="abs brand"><span>Chemora</span><span class="brand-dot"></span></div>
  <nav class="abs main-nav">
    <a class="active" href="#">HOME</a><a href="#">ABOUT US</a><a href="#">SERVICES</a><a href="#">WHAT WE DO</a><a href="#">BLOG</a><a href="#">CONTACT US</a>
  </nav>
  <div class="abs search-toggle">
    <svg width="10" height="10" viewBox="0 0 10 10"><circle cx="4" cy="4" r="2.8" fill="none" stroke="#fff" stroke-width="1.4"/><line x1="6" y1="6" x2="9" y2="9" stroke="#fff" stroke-width="1.6"/></svg>
  </div>
</header>

<section class="abs hero" role="img" aria-label="Laboratory scientist in protective suit, goggles and mask holding a test tube"></section>
<h1 class="abs hero-title">A CHEMICAL DISTRIBUTION COMPANY</h1>
<svg class="abs hero-arrow" style="left:56px" width="12" height="18" viewBox="0 0 12 18"><polyline points="9,2 3,9 9,16" fill="none" stroke="#fff" stroke-width="2.5"/></svg>
<svg class="abs hero-arrow" style="left:740px" width="12" height="18" viewBox="0 0 12 18"><polyline points="3,2 9,9 3,16" fill="none" stroke="#fff" stroke-width="2.5"/></svg>

<div class="abs search-bar"></div>
<div class="abs search-label">Search</div>
<div class="abs field" style="left:145px;width:241px">Chemicals</div>
<div class="abs field" style="left:395px;width:219px">Locations</div>
<div class="abs search-btn">SEARCH NOW</div>

<div class="abs industries"></div>
<div class="abs industry-icon" style="left:98px">
  <svg width="24" height="36" viewBox="0 0 24 36"><rect x="8" y="0" width="8" height="5" fill="#fff"/><rect x="6" y="6" width="12" height="5" fill="#fff"/><rect x="2" y="12" width="20" height="24" rx="3" fill="#fff"/></svg>
</div>
<div class="abs industry-shadow" style="left:105px"></div>
<div class="abs industry-title" style="left:181px">PLASTIC</div>
<p class="abs industry-text" style="left:181px">Neque porro quisquam est qui dolorem ipsum quia dolor sit amet, consectetur, adipisci velit...</p>

<div class="abs industry-icon" style="left:306px">
  <svg width="46" height="28" viewBox="0 0 46 28"><ellipse cx="22" cy="8" rx="20" ry="6" fill="none" stroke="#fff" stroke-width="3"/><ellipse cx="22" cy="8" rx="8" ry="2.5" fill="#fff"/><path d="M2 8v10c0 3 9 6 20 6s20-3 20-6V8" fill="none" stroke="#fff" stroke-width="3"/><rect x="34" y="14" width="10" height="6" fill="#fff"/></svg>
</div>
<div class="abs industry-shadow" style="left:313px"></div>
<div class="abs industry-title" style="left:384px">RESIN</div>
<p class="abs industry-text" style="left:385px">Neque porro quisquam est qui dolorem ipsum quia dolor sit amet, consectetur, adipisci velit...</p>

<div class="abs industry-icon" style="left:518px">
  <svg width="36" height="36" viewBox="0 0 36 36"><rect x="6" y="6" width="6" height="14" fill="#fff"/><rect x="15" y="6" width="6" height="14" fill="#fff"/><polygon points="2,20 34,14 34,36 2,36" fill="#fff"/><rect x="7" y="28" width="4" height="4" fill="#0a6fc2"/><rect x="14" y="28" width="4" height="4" fill="#0a6fc2"/><rect x="21" y="28" width="4" height="4" fill="#0a6fc2"/></svg>
</div>
<div class="abs industry-shadow" style="left:525px"></div>
<div class="abs industry-title" style="left:597px">INDUSTRIAL</div>
<p class="abs industry-text" style="left:598px">Neque porro quisquam est qui dolorem ipsum quia dolor sit amet, consectetur, adipisci velit...</p>

<h2 class="abs section-title" style="left:98px;font-weight:400">WELCOME TO CHEMORA</h2>
<div class="abs welcome-photo" role="img" aria-label="Scientist in safety glasses examining a flask of green liquid"></div>
<p class="abs body-copy" style="left:97px;top:866px;width:400px">Sed ut perspiciatis unde omnis iste natus error sit voluptatem accusantium doloremque laudantium, totam rem aperiam, eaque ipsa quae ab illo inventore veritatis et quasi architecto beatae vitae dicta sunt explicabo. Nemo enim ipsam voluptatem quia voluptas sit aspernatur aut odit aut fugit, sed quia consequuntur magni dolores eos qui ratione voluptatem sequi nesciunt. Neque porro quisquam est, qui dolorem ipsum quia dolor sit amet .</p>
<div class="abs btn" style="left:98px;top:937px;width:62px">Read More</div>

<h2 class="abs section-title" style="left:518px;font-weight:400">BLOG</h2>
<div class="abs pager">‹›</div>
<div class="abs blog-photo" role="img" aria-label="Microscope with green leaf sample and DNA helix graphic"></div>
<div class="abs date-badge">FEB<br>16TH<br>2015</div>
<p class="abs blog-heading">Sed ut perspiciatis unde omnis iste natus error sit voluptatem accusantium doloremque</p>
<p class="abs body-copy" style="left:516px;top:887px;width:196px">Sed ut perspiciatis unde omnis iste natus error sit voluptatem accusantium doloremque laudantium, totam rem aperiam, eaque ipsa quae ab illo inventore</p>
<div class="abs btn" style="left:518px;top:937px;width:62px">Read More</div>

<div class="abs ad-banner" role="img" aria-label="Pipette dropping blue liquid into glass laboratory flasks"></div>
<div class="abs ad-brand"><span>Chemora</span><span class="brand-dot"></span></div>
<div class="abs ad-title">Chemora</div>
<div class="abs ad-sub">a chemical distribution company</div>
<div class="abs ad-tag">Ads</div>

<footer class="abs site-footer"></footer>
<div class="abs social"><span></span><span></span><span></span><span></span><span></span><span></span></div>
<nav class="abs footer-nav">HOME<i>|</i>ABOUT US<i>|</i>SERVICES<i>|</i>WHAT WE DO<i>|</i>BLOG<i>|</i>CONTACT US</nav>
<p class="abs copyright">© 2016 COMPANY NAME &nbsp;| ALL RIGHTS RESERVED</p>

</body>
</html>
```